Zanquorra Business Card Design

Zanquorra is a small and new restaurant/ bar location in Hong Kong. The name "Djibouti" derives from an African country. There is no specific reason behind other than the fact, that the bar is somewhat inspired by African elements (only inspired but not purely based on African cuisine etc.).

The bar is somewhat a fusion of African, Mediterranean and Oriental (Old French Vietnam) elements.

However, it is very imperative to stress, that the overall look and feel of Zanquorra is a very high end cocktail lounge/ bar location. The bar is tucked away in a hidden alley, so people will have to know about it. The idea is to send the consumer off in an Escape or hidden remote location where they are at ease in a hip, stylish and trendy environment.

The card needs to feel high-end.

Final logo artwork has been attached and also pictures of the bar/ restaurant itself. The logo ie monkey head cannot be modified. However, the background color and the color of the type "ZANQUORRA" can be changed.

The following details need to fit onto the business card. Of course they can be arranged to your liking:

LOGO

Colin Vey
Partner

+852 97035164
xxx@zanquorra.com
www.zanquorra.com
7C, Brennick Road, Wan Chai, Hong Kong

```html
<!DOCTYPE html>
<html lang="en">
<head>
<meta charset="utf-8">
<title>Zanquorra Business Card</title>
<link rel="stylesheet" href="https://fonts.googleapis.com/css2?family=Cinzel:wght@400;600&display=swap">
<style>
  :root {
    --backdrop: #e8e8e8;
    --plum-deep: #240a18;
    --plum: #4c1633;
    --plum-glow: #5e1c40;
    --ink-black: #0b0609;
    --flourish: #6a1a45;
    --text-light: #ece2e7;
    --accent: #8e2d60;
    --wordmark: #1f0c17;
    --disc: #f4eee3;
    --disc-ring: #2b1822;
  }
  * { box-sizing: border-box; margin: 0; padding: 0; }
  html, body { width: 1200px; height: 1000px; overflow: hidden; }
  body {
    background: var(--backdrop);
    font-family: 'Cinzel', serif;
    position: relative;
  }
  .card {
    position: absolute;
    left: 250px;
    width: 700px;
    height: 400px;
    overflow: hidden;
    box-shadow: 0 6px 18px rgba(0,0,0,0.18);
  }
  /* Front */
  .card-front {
    top: 60px;
    background: radial-gradient(ellipse at 50% 40%, var(--plum-glow) 0%, var(--plum) 45%, var(--plum-deep) 100%);
  }
  .card-front .texture {
    position: absolute; inset: 0;
    background: radial-gradient(ellipse at 50% 45%, rgba(120,40,85,0.18), rgba(0,0,0,0.25));
  }
  .brand-disc {
    position: absolute;
    left: 50%; top: 40px;
    width: 200px; height: 200px;
    margin-left: -100px;
    border-radius: 50%;
    background: var(--disc);
    border: 8px solid var(--disc-ring);
    box-shadow: 0 0 22px rgba(255,220,240,0.35);
  }
  .wordmark {
    position: absolute;
    left: 0; right: 0; top: 268px;
    text-align: center;
    font-size: 64px;
    font-weight: 600;
    letter-spacing: 4px;
    color: var(--wordmark);
  }
  /* Back */
  .card-back {
    top: 540px;
    background: linear-gradient(90deg, var(--ink-black) 0%, var(--ink-black) 30%, #1c0a14 60%, #2c0d1f 100%);
  }
  .card-back .flourish-field {
    position: absolute;
    top: 0; right: 0; bottom: 0; width: 62%;
    background: linear-gradient(90deg, rgba(106,26,69,0) 0%, rgba(106,26,69,0.35) 40%, rgba(106,26,69,0.55) 100%);
  }
  .contact {
    position: absolute;
    left: 46px; top: 232px;
    color: var(--text-light);
  }
  .contact .name { font-size: 17px; letter-spacing: 0.5px; }
  .contact .role { font-size: 10px; color: var(--accent); margin-top: 1px; }
  .contact .details { list-style: none; margin-top: 26px; font-size: 14px; line-height: 19px; }
</style>
</head>
<body>
  <section class="card card-front">
    <div class="texture" role="img" aria-label="Faint damask flourish pattern in deep plum"></div>
    <div class="brand-disc"></div>
    <div class="wordmark">ZANQUORRA</div>
  </section>

  <section class="card card-back">
    <div class="flourish-field" role="img" aria-label="Ornate plum damask flourish pattern fading in from the right"></div>
    <div class="contact">
      <div class="name">Colin Vey</div>
      <div class="role">Partner</div>
      <ul class="details">
        <li>+852 97035164</li>
        <li>xxx@zanquorra.com</li>
        <li>www.zanquorra.com</li>
        <li>7C, Brennick Road, Wan Chai, Hong Kong</li>
      </ul>
    </div>
  </section>
</body>
</html>
```